New Shopify design for existing webshop

We have an existing webshop on an old Magento solution. Now we're going to switch to Shopify. We need a new Shopify theme for this.

Our old website is www.tessin-brand.ch

We have the product categories:
Postage stamps
Tobler albums & accessories
Coins and banknotes
Franking service

In addition, we need the pages to be prominently integrated similar to the products:
Missing list service
Purchases

We can include the following pages at the bottom, less prominently on the page:
Contact
imprint
Conditions
revocation
data protection

shipping
Guarantee of trust

The products should be in the foreground on the website. Our logo can be incorporated. We also upload some images that can be used for the design. Of course you don't have to.

The new design does not have to be based on the old design. It can be something completely new. All pictures that we have on the website can of course also be used. But I also added some pictures to the project that fit our company.

Our company:
The company, which was founded by Paul Tobler in 1922, has developed into one of the largest and best-known Swiss postage stamp houses over the past 98 years.

Target Market(s)

Germany, Switzerland

Font styles to use
Serif
Sans Serif

Requirements
Must have
• The products stamps that you can buy should be in the foreground.
If images are used in the design, please focus on Swiss stamps and coins (no foreign coins or stamps)

```html
<!DOCTYPE html>
<html lang="en">
<head>
<meta charset="utf-8">
<title>Tobler Philatelie – Ancient Coin Collection</title>
<link href="https://fonts.googleapis.com/css2?family=Poppins:wght@400;500&family=Playfair+Display:wght@700&family=Montserrat:wght@400&display=swap" rel="stylesheet">
<style>
  :root {
    --brand-red: #ec1c24;
    --ink: #333333;
    --white: #ffffff;
    --hero-bg: #242424;
    --gold-light: #f3e3b0;
    --gold-deep: #c9a862;
    --badge-grey: #9b9b9b;
  }
  * { margin: 0; padding: 0; box-sizing: border-box; }
  html, body { width: 1200px; height: 649px; overflow: hidden; background: var(--white); }
  body { position: relative; font-family: "Poppins", sans-serif; color: var(--ink); }

  .site-header { position: absolute; left: 0; top: 0; width: 1200px; height: 100px; background: var(--white); }
  .brand {
    position: absolute; left: 164px; top: 38px;
    font-family: "Poppins", sans-serif; font-weight: 500; font-size: 17px;
    color: var(--ink); white-space: nowrap;
  }

  .main-nav { position: absolute; left: 362px; top: 45px; display: flex; }
  .main-nav a { font-size: 9.6px; color: var(--ink); text-decoration: none; margin-right: 19.5px; white-space: nowrap; }

  .utility { position: absolute; top: 43px; left: 944px; display: flex; align-items: center; }
  .cart-icon { position: relative; width: 12px; height: 12px; }
  .cart-count {
    position: absolute; left: 3px; top: -13px; width: 11px; height: 11px; border-radius: 50%;
    background: var(--badge-grey); color: var(--white); font-size: 7px; line-height: 11px; text-align: center;
  }
  .cart-label { font-size: 9.6px; margin-left: 15px; }
  .icon-btn { margin-left: 18px; width: 10px; height: 10px; display: block; }

  .hero { position: absolute; left: 0; top: 100px; width: 1200px; height: 549px; background: var(--hero-bg); }
  .coin-visual { position: absolute; left: 389px; top: 46px; width: 422px; height: 208px; display: flex; justify-content: space-between; }
  .coin-visual span {
    width: 208px; height: 208px; border-radius: 50%;
    background: radial-gradient(circle at 45% 40%, var(--gold-light), var(--gold-deep));
  }
  .slider-arrow { position: absolute; top: 211px; width: 27px; height: 16px; }
  .slider-arrow.prev { left: 121px; }
  .slider-arrow.next { left: 1053px; }

  .hero-title {
    position: absolute; left: 0; width: 1200px; top: 311px; text-align: center;
    font-family: "Playfair Display", serif; font-weight: 700; font-size: 32px; color: var(--brand-red);
  }
  .hero-subtitle {
    position: absolute; left: 0; width: 1200px; top: 362px; text-align: center;
    font-family: "Poppins", sans-serif; font-weight: 500; font-size: 20px; color: var(--white);
  }
  .hero-cta {
    position: absolute; left: 465px; top: 430px; width: 270px; height: 36px;
    background: var(--brand-red); color: var(--white);
    font-family: "Montserrat", sans-serif; font-size: 16px; letter-spacing: 0.5px;
    display: flex; align-items: center; justify-content: center; text-decoration: none;
  }
</style>
</head>
<body>
  <header class="site-header">
    <div class="brand">Tobler Philatelie</div>
    <nav class="main-nav">
      <a href="#">Home</a>
      <a href="#">Postage stamps</a>
      <a href="#">Tobler albums &amp; accessories</a>
      <a href="#">Coins and banknotes</a>
      <a href="#">Franking service</a>
    </nav>
    <div class="utility">
      <div class="cart-icon">
        <span class="cart-count">0</span>
        <svg width="10" height="11" viewBox="0 0 10 11"><path d="M3 3V2a2 2 0 0 1 4 0v1h2l.5 8H.5L1 3z M4 3h2V2a1 1 0 0 0-2 0z" fill="#333" fill-rule="evenodd"/></svg>
      </div>
      <span class="cart-label">Cart</span>
      <svg class="icon-btn" viewBox="0 0 10 10"><circle cx="4" cy="4" r="3" fill="none" stroke="#333" stroke-width="1.6"/><path d="M6.2 6.2 9 9" stroke="#333" stroke-width="1.8" stroke-linecap="round"/></svg>
      <svg class="icon-btn" viewBox="0 0 10 10" style="margin-left:16px"><path d="M1 2h8M1 5h8M1 8h8" stroke="#333" stroke-width="1.6"/></svg>
    </div>
  </header>

  <section class="hero">
    <div class="coin-visual" role="img" aria-label="Swiss 20 franc gold coin, obverse and reverse"><span></span><span></span></div>
    <svg class="slider-arrow prev" viewBox="0 0 27 16"><path d="M27 6H10V1L0 8l10 7v-5h17z" fill="#ec1c24"/></svg>
    <svg class="slider-arrow next" viewBox="0 0 27 16"><path d="M0 6h17V1l10 7-10 7v-5H0z" fill="#ec1c24"/></svg>
    <h1 class="hero-title">Ancient Coin Collection</h1>
    <p class="hero-subtitle">buy or sell ancient coins</p>
    <a class="hero-cta" href="#">KNOW MORE</a>
  </section>
</body>
</html>
```